New Menu Design Project

Would like a menu designed..

SIZE A4 - double sided..

One on side, we would like our regular menu, on the other side we would like our catering options.
I have attached both files/
I have also attached our logo

Target Market(s)

We are located at a hospital, so we target hospital staff and also university students.

Industry/Entity Type

Catering

```html
<!DOCTYPE html>
<html lang="en">
<head>
<meta charset="utf-8">
<title>Wardside Menu</title>
<link rel="stylesheet" href="https://fonts.googleapis.com/css2?family=Montserrat:wght@800&family=Oswald:wght@500;600&family=Didact+Gothic&display=swap">
<style>
  :root {
    --cream: #f6f2e4;
    --paper: #ffffff;
    --ink: #1f1f1f;
    --slate: #4c5258;
    --red: #e4032e;
    --tan: #e8deb3;
    --tan-ink: #5a5a55;
  }
  * { margin: 0; padding: 0; box-sizing: border-box; }
  html, body { width: 848px; height: 1200px; overflow: hidden; background: var(--cream); }
  body { font-family: "Didact Gothic", "Century Gothic", sans-serif; color: var(--ink); }
  .menu-page { position: relative; width: 848px; height: 1200px; overflow: hidden; background: var(--cream); }

  .menu-title {
    position: absolute; left: 62px; top: 18px;
    font-family: "Montserrat", sans-serif; font-weight: 800;
    font-size: 72px; letter-spacing: 6px; color: var(--slate); line-height: 1;
  }
  .preorder {
    position: absolute; left: 62px; top: 92px;
    font-size: 19px; letter-spacing: 0.3px;
  }
  .preorder strong { font-family: "Montserrat", sans-serif; font-weight: 800; margin: 0 4px; }

  .menu-panel {
    position: absolute; left: 40px; top: 131px; width: 768px; height: 930px;
    background: var(--paper); border: 3px solid var(--red);
  }

  .brand {
    position: absolute; left: 575px; top: 52px;
    display: flex; align-items: center; gap: 12px;
  }
  .brand-dot { width: 34px; height: 34px; border-radius: 50%; background: var(--red); }
  .brand-name {
    font-family: "Oswald", sans-serif; font-weight: 600; font-size: 50px;
    color: var(--red); letter-spacing: 1px; line-height: 1;
  }

  .section-title {
    position: absolute;
    font-family: "Oswald", sans-serif; font-weight: 500; font-size: 24px;
    letter-spacing: 0.2px; line-height: 1; text-transform: uppercase;
  }
  .section-title small { font-size: 15px; }

  .item-list { position: absolute; list-style: none; font-size: 19px; }
  .item-list li { position: relative; height: 28.5px; line-height: 28.5px; white-space: nowrap; }
  .item-list .price { position: absolute; top: 0; }
  .item-list .indent { padding-left: 37px; }
  .item-list em { font-size: 17px; }

  .light-list .price { left: 250px; }
  .hot-list .price { left: 270px; }
  .hot-list .price.cents { left: 300px; }
  .breakfast-list .price { left: 270px; }

  .burger-list { position: absolute; left: 446px; top: 726px; width: 330px; list-style: none; }
  .burger-list li { position: relative; margin-bottom: 7px; }
  .burger-name { font-size: 19px; line-height: 24px; }
  .burger-desc { font-style: italic; font-size: 15.5px; line-height: 21px; color: #333; width: 262px; }
  .burger-list .price { position: absolute; right: 34px; bottom: 0; font-size: 19px; line-height: 21px; }
  .burger-list .extras { padding-bottom: 20px; }
  .burger-list .extras .price { bottom: auto; top: 24px; right: 24px; }
  .burger-list .per-item { position: absolute; right: 24px; top: 45px; font-style: italic; font-size: 15.5px; line-height: 20px; }

  .icon-slot { position: absolute; background: var(--slate); }
  .plate-slot { left: 168px; top: 385px; width: 92px; height: 92px; border-radius: 50%; }
  .cross-slot { left: 534px; top: 644px; width: 108px; height: 20px; background: var(--red); opacity: 0.85; }

  .catering-band {
    position: absolute; left: 28px; top: 938px; width: 880px; height: 120px;
    background: var(--tan); transform: rotate(8.7deg); transform-origin: left top;
  }
  .band-dots { position: absolute; left: 222px; top: 46px; display: flex; gap: 33px; }
  .band-dots i, .band-dots-end i { display: block; width: 10px; height: 10px; border-radius: 50%; background: var(--red); }
  .band-dots-end { position: absolute; left: 676px; top: 60px; display: flex; gap: 33px; }
  .band-copy { position: absolute; left: 290px; top: 0; width: 420px; color: var(--tan-ink); text-align: center; }
  .band-kicker { font-family: "Oswald", sans-serif; font-size: 24px; letter-spacing: 8px; line-height: 32px; }
  .band-headline { font-family: "Oswald", sans-serif; font-weight: 600; font-size: 60px; letter-spacing: 3px; line-height: 60px; color: var(--slate); }
  .band-note { font-family: "Oswald", sans-serif; font-size: 19px; letter-spacing: 7px; line-height: 26px; white-space: nowrap; }
  .cloche-slot { left: 66px; top: 968px; width: 150px; height: 100px; border-radius: 75px 75px 6px 6px; }

  .hours-label { position: absolute; left: 62px; top: 1096px; font-size: 17px; line-height: 20px; }
  .contact-email { position: absolute; left: 62px; top: 1164px; font-size: 17px; }
</style>
</head>
<body>
<main class="menu-page">
  <h1 class="menu-title">MENU</h1>
  <p class="preorder">PHONE OR TEXT <strong>0491 570 156</strong> TO PRE ORDER</p>

  <section class="menu-panel" aria-label="Menu items"></section>

  <div class="brand">
    <span class="brand-dot" aria-hidden="true"></span>
    <span class="brand-name">WARDSIDE</span>
  </div>

  <h2 class="section-title" style="left:61px;top:154px;">Something Light</h2>
  <ul class="item-list light-list" style="left:61px;top:188px;">
    <li>Mixed yoghurts<span class="price">$5.50</span></li>
    <li>Chia puddings<span class="price">$5.50</span></li>
    <li>Fruit salad<span class="price">$5.50</span></li>
    <li>Bircher muesli<span class="price">$5.50</span></li>
    <li>Homemade muffins<span class="price">$4.50</span></li>
    <li>Banana bread<span class="price">$4.50</span></li>
    <li>Slices<span class="price">$4</span></li>
    <li>Cookies<span class="price">$3-$4</span></li>
  </ul>
  <div class="icon-slot plate-slot" role="img" aria-label="Plate with knife and fork icon"></div>

  <h2 class="section-title" style="left:61px;top:509px;">Hot Food <small>AND</small> Sandwiches</h2>
  <ul class="item-list hot-list" style="left:61px;top:544px;">
    <li>Pre made sandwiches<span class="price">$6.00</span></li>
    <li>Focaccias<span class="price">$7.50</span></li>
    <li>Parma roll<span class="price">$9.00</span></li>
    <li>Salad with meat or seafood<span class="price">$9.50</span></li>
    <li>Vegetarian salad<span class="price">$7.50</span></li>
    <li>Light meals $7.50 <em>add salad</em> $2.00</li>
    <li>Hot Chips<span class="price">$4.50</span></li>
    <li>Spring roll<span class="price">$3.00</span></li>
    <li>Dim sim<span class="price">$1.50</span></li>
    <li>Potato cake<span class="price">$1.50</span></li>
    <li>Hash brown<span class="price">$1.50</span></li>
    <li>Homemade sausage rolls<span class="price" style="left:276px">$4.50</span></li>
    <li>Sauce sachet<span class="price cents">30¢</span></li>
    <li>Gravy<span class="price cents">50¢</span></li>
  </ul>

  <h2 class="section-title" style="left:446px;top:305px;">Breakfast Items</h2>
  <ul class="item-list breakfast-list" style="left:446px;top:338px;">
    <li>Egg, bacon &amp; cheese roll<span class="price">$6</span></li>
    <li>Ham &amp; cheese toastie<span class="price">$5.50</span></li>
    <li>Cheese &amp; tomato toastie<span class="price">$5</span></li>
    <li>Ham &amp; cheese croissant<span class="price">$6.00</span></li>
    <li>Cheese &amp; tomato croissant<span class="price">$5.50</span></li>
    <li>Plain croissant<span class="price">$3.50</span></li>
    <li class="indent">Toasted with spreads<span class="price">$4</span></li>
    <li>Hash brown<span class="price">$1.50</span></li>
    <li>2 piece toast with spreads<span class="price">$3</span></li>
    <li>2 piece rasin toast<span class="price">$3</span></li>
  </ul>
  <div class="icon-slot cross-slot" role="img" aria-label="Row of three red cross marks"></div>

  <h2 class="section-title" style="left:446px;top:690px;">Burgers</h2>
  <ul class="burger-list">
    <li>
      <div class="burger-name">Plain hamburger</div>
      <div class="burger-desc">tomato, onion, lettuce, sauce</div>
      <span class="price">$7.50</span>
    </li>
    <li>
      <div class="burger-name">Hamburger with the lot</div>
      <div class="burger-desc">plain plus beetroot, egg, cheese and bacon</div>
      <span class="price">$9.00</span>
    </li>
    <li>
      <div class="burger-name">Schnitzel burger</div>
      <div class="burger-desc">homemade breast fillet schnitzel with lettuce, cheese, mayo</div>
      <span class="price">$7.50</span>
    </li>
    <li class="extras">
      <div class="burger-name">Extras</div>
      <div class="burger-desc">beetroot, egg, cheese, bacon</div>
      <span class="price">50¢-$1</span>
      <span class="per-item">per item</span>
    </li>
  </ul>

  <div class="catering-band">
    <div class="band-dots"><i></i><i></i><i></i></div>
    <div class="band-copy">
      <div class="band-kicker">WE OFFER</div>
      <div class="band-headline">CATERING!</div>
      <div class="band-note">SEE REVERSE SIDE FOR DETAILS</div>
    </div>
    <div class="band-dots-end"><i></i><i></i><i></i></div>
  </div>
  <div class="icon-slot cloche-slot" role="img" aria-label="Serving cloche icon"></div>

  <p class="hours-label">DAYS AND HOURS<br>OF OPERATION</p>
  <p class="contact-email">ORDERS@WARDSIDE.COM.AU</p>
</main>
</body>
</html>
```